BriarLoom Website Homepage Design

Please provide your idea of homepage for a hosting company. This project is for DESIGN only, no coding.

It must use/combine colors used in logo, clean, modern look.

Homepage must consist of at least 4 sections (example: testimonials, services, and so on. not necesarily all of them). We would like the navigation to be horizontal, but not mandatory.

You can include a preview of services page (optional, not a must).

Number of Pages Required

1 page

Font styles to use
Sans Serif

```html
<!DOCTYPE html>
<html lang="en">
<head>
<meta charset="utf-8">
<title>BriarLoom – Hosting Homepage</title>
<link href="https://fonts.googleapis.com/css2?family=Montserrat:wght@300;400;500;600;700;800&display=swap" rel="stylesheet">
<style>
:root{
  --blue-deep:#0a58b4;
  --blue:#1a8ad4;
  --blue-bright:#2196e0;
  --ice:#ebf6fb;
  --mist:#dcedf5;
  --ink:#111418;
  --grey:#555b63;
  --white:#ffffff;
  --black:#000000;
}
*{box-sizing:border-box;margin:0;padding:0}
html,body{width:1200px;height:3000px;overflow:hidden;background:var(--white)}
body{font-family:'Montserrat',sans-serif;color:var(--ink)}
.canvas{position:relative;width:1200px;height:3000px;overflow:hidden;background:var(--white)}
.side-bands{position:absolute;left:0;top:0;width:1200px;height:3000px}
.section{position:absolute;left:150px;width:900px}

/* hero */
.hero{top:0;height:495px;background:linear-gradient(120deg,#1b2230 0%,#2c3340 35%,#5a4634 60%,#3b2f2c 80%,#1d2027 100%)}
.hero-photo{position:absolute;inset:0;background:radial-gradient(circle at 78% 40%,rgba(190,120,80,.45),transparent 45%),radial-gradient(circle at 30% 70%,rgba(230,150,60,.25),transparent 40%)}
.hero-base{position:absolute;left:0;bottom:0;width:900px;height:5px;background:#7b8088}
.logo{font-family:'Montserrat',sans-serif;font-weight:700;color:var(--blue-bright);letter-spacing:1px}
.nav{position:absolute;top:16px;left:0;width:900px;height:30px}
.nav .logo{position:absolute;left:76px;top:2px;font-size:27px}
.nav a{position:absolute;top:8px;color:var(--white);font-size:11.5px;font-weight:600;text-decoration:none}
.nav .cta{top:0;left:726px;width:80px;height:28px;background:var(--blue);display:flex;align-items:center;justify-content:center}
.nav .cta-frame{position:absolute;left:731px;top:4px;width:82px;height:30px;border:1px solid var(--white)}
.hero-title{position:absolute;left:72px;top:144px;color:var(--white);font-size:36px;line-height:42px}
.hero-title b{font-weight:700;display:block}
.hero-title span{font-weight:400;display:block}
.hero-text{position:absolute;left:72px;top:243px;width:390px;color:var(--white);font-size:13px;line-height:21px;font-weight:500}
.btn{position:absolute;background:var(--blue);color:var(--white);display:flex;align-items:center;justify-content:center;font-weight:500}
.btn-frame{position:absolute;border:1.5px solid var(--white)}
.arrow{position:absolute;width:20px;height:20px}
.dots{position:absolute;left:427px;top:461px;display:flex;gap:6px}
.dots i{width:8px;height:8px;border-radius:50%;background:var(--white);display:block}

/* services */
.services{top:495px;height:763px;background:var(--ice)}
.sec-title{position:absolute;left:0;width:900px;text-align:center;font-weight:800;font-size:30px;letter-spacing:.5px}
.rule{position:absolute;height:2px;background:var(--ink)}
.service{position:absolute;width:200px;text-align:center}
.service .disc{width:84px;height:84px;border-radius:50%;background:var(--blue-bright);border:2px solid #4aaae8;margin:0 auto 12px;display:flex;align-items:center;justify-content:center}
.service h3{font-size:12.5px;font-weight:700;margin-bottom:5px}
.service p{font-size:8.5px;line-height:10.5px;color:var(--grey)}
.service a{display:block;margin-top:10px;font-size:9.5px;font-weight:700;color:var(--ink);text-decoration:none}
.center-photo{position:absolute;left:319px;top:369px;width:264px;height:264px;border-radius:50%;background:radial-gradient(circle at 50% 45%,#5cb0e8,#2b8fd5 70%);border:3px solid var(--white);box-shadow:0 0 0 1px #bfe0f4}

/* about */
.about{top:1258px;height:443px}
.about h2{position:absolute;left:72px;top:58px;font-size:30px;font-weight:800}
.about p{position:absolute;left:72px;top:131px;width:286px;font-size:12.4px;line-height:15.7px;color:var(--ink)}
.about .btn{left:72px;top:337px;width:106px;height:33px;font-size:15px}
.about .btn-frame{left:88px;top:344px;width:106px;height:33px;border-color:var(--ink)}
.photo-back{position:absolute;left:497px;top:56px;width:337px;height:224px;background:linear-gradient(110deg,#3a4048,#6d7378 50%,#9aa0a4)}
.photo-front{position:absolute;left:414px;top:143px;width:261px;height:181px;background:linear-gradient(120deg,#e9b07a,#c9774f 40%,#7a6a5c 75%,#4c6e5e)}
.photo-frame{position:absolute;left:466px;top:181px;width:236px;height:163px;border:1.5px solid var(--blue)}

/* testimonials */
.testimonials{top:1701px;height:429px;background:linear-gradient(90deg,#1b1c20,#2a2c31 50%,#1a1b1f)}
.testimonials .sec-title{color:var(--white);top:45px}
.testimonials .sub{position:absolute;left:0;width:900px;top:98px;text-align:center;color:var(--white);font-size:22px;font-weight:300}
.quote-card{position:absolute;top:160px;width:322px;height:152px;background:var(--white);border-radius:5px}
.quote-card::after{content:"";position:absolute;left:48px;bottom:-16px;border-right:22px solid transparent;border-top:17px solid var(--white)}
.quote-card svg{position:absolute;left:28px;top:18px}
.quote-card p{position:absolute;left:20px;top:42px;width:296px;font-size:10.6px;line-height:15px;color:#333;text-indent:60px}
.author{position:absolute;top:333px;display:flex;align-items:center;gap:12px;color:var(--white)}
.author .ava{width:42px;height:42px;border-radius:50%;background:linear-gradient(#d9d4cf,#9e948c);border:2px solid var(--white)}
.author b{display:block;font-size:11px;font-weight:700}
.author span{display:block;font-size:10.5px;font-weight:400}

/* pricing */
.pricing{top:2130px;height:567px;background:var(--mist)}
.pricing .sec-title{top:70px;font-size:30px}
.pricing .lead{position:absolute;left:150px;width:600px;top:131px;text-align:center;font-size:12px;line-height:14.5px;color:#5b7f9e}
.plan{position:absolute;top:214px;width:178px;height:260px;background:var(--white);text-align:center;border-radius:3px}
.plan .ic{height:46px;margin-top:24px;display:flex;justify-content:center}
.plan h4{margin-top:16px;font-size:12.5px;font-weight:500}
.plan p{margin:10px auto 0;width:130px;font-size:7.8px;line-height:9.5px;color:#555}
.plan hr{border:0;border-top:1px solid #c9c9c9;width:136px;margin:12px auto 0}
.plan .price{margin-top:10px;font-size:12.5px;font-weight:500}
.plan .price em{font-style:normal;color:var(--blue);font-weight:700;margin-right:8px}
.plan .go{margin:16px auto 0;width:136px;height:25px;background:var(--blue);color:var(--white);font-size:9.5px;display:flex;align-items:center;justify-content:center;letter-spacing:.5px}
.plan.featured{background:var(--blue);color:var(--white)}
.plan.featured h4,.plan.featured .price{font-weight:700}
.plan.featured p{color:var(--white)}
.plan.featured hr{border-top-color:rgba(255,255,255,.6)}
.plan.featured .price em{color:var(--white)}
.plan.featured .go{background:var(--white);color:var(--ink)}

/* footer */
.footer{top:2697px;height:303px;background:var(--black);color:var(--white)}
.footer .logo{position:absolute;left:97px;top:50px;font-size:33px}
.footer .about-text{position:absolute;left:97px;top:109px;width:250px;font-size:12px;line-height:14px}
.footer .follow{position:absolute;left:97px;top:182px;font-size:12px;font-weight:700}
.social{position:absolute;top:209px;width:34px;height:34px;border-radius:50%;background:var(--white);display:flex;align-items:center;justify-content:center}
.social i{width:14px;height:14px;border-radius:3px;background:var(--blue);display:block}
.fcol{position:absolute;top:73px;font-size:12px}
.fcol h5{font-size:12px;font-weight:700;margin-bottom:24px}
.fcol ul{list-style:none}
.fcol li{height:36.7px}
.footer .divider{position:absolute;left:95px;top:263px;width:710px;height:1px;background:#555}
.copyright{position:absolute;left:0;width:900px;top:277px;text-align:center;font-size:8px;color:#5f5f5f}
.copyright span{display:inline-block;width:1px;height:12px;background:#555;vertical-align:middle;margin:0 8px}
</style>
</head>
<body>
<div class="canvas">

  <svg class="side-bands" viewBox="0 0 1030 2576" preserveAspectRatio="none" aria-hidden="true">
    <g fill="#0a58b4">
      <polygon points="901,100 1030,60 1030,290 901,340"/>
      <polygon points="901,385 1030,335 1030,570 901,625"/>
      <polygon points="901,1415 1030,1355 1030,1640 901,1700"/>
      <polygon points="901,1745 1030,1690 1030,1890 901,1950"/>
      <polygon points="0,520 129,460 129,700 0,755"/>
      <polygon points="0,790 129,735 129,990 0,1045"/>
      <polygon points="0,1835 129,1780 129,2010 0,2065"/>
      <polygon points="0,2100 129,2075 129,2310 0,2365"/>
    </g>
  </svg>

  <!-- Hero -->
  <header class="section hero">
    <div class="hero-photo" role="img" aria-label="Woman holding a tablet behind a window with glowing city lights at night"></div>
    <nav class="nav">
      <div class="logo">BriarLoom</div>
      <a style="left:376px">Home</a>
      <a style="left:448px">About Us</a>
      <a style="left:534px">Our Services</a>
      <a style="left:638px">Testimonial</a>
      <div class="cta-frame"></div>
      <a class="cta">Contact Us</a>
    </nav>
    <h1 class="hero-title"><b>Hosting Data</b><span>Service</span></h1>
    <p class="hero-text">Lorem Ipsum Dolor Sit Amet, Consectetur Adipiscing Elit, Sed Do Eiusmod Tempor Incididunt Ut Labore Et Dolore Magna Aliqua. Ut Enim Ad Minim Veniam,</p>
    <div class="btn-frame" style="left:85px;top:357px;width:140px;height:32px"></div>
    <div class="btn" style="left:72px;top:347px;width:140px;height:33px;font-size:16px">Learn More</div>
    <svg class="arrow" style="left:32px;top:232px" viewBox="0 0 20 20"><path d="M13 3 6 10l7 7" fill="none" stroke="#fff" stroke-width="3.5"/></svg>
    <svg class="arrow" style="left:860px;top:232px" viewBox="0 0 20 20"><path d="M7 3l7 7-7 7" fill="none" stroke="#fff" stroke-width="3.5"/></svg>
    <div class="dots"><i></i><i></i><i></i><i></i></div>
    <div class="hero-base"></div>
  </header>

  <!-- Services -->
  <section class="section services">
    <h2 class="sec-title" style="top:80px">OUR SERVICES</h2>
    <div class="rule" style="left:364px;top:129px;width:176px"></div>

    <div class="service" style="left:351px;top:163px">
      <div class="disc"><svg width="46" height="46" viewBox="0 0 46 46" fill="none" stroke="#fff" stroke-width="2.4"><path d="M8 18h30M14 18l3-10h12l3 10"/><circle cx="15" cy="30" r="6"/><circle cx="31" cy="30" r="6"/><path d="M21 30h4"/></svg></div>
      <h3>Private Networking</h3>
      <p>"Lorem Ipsum Dolor Sit Amet,<br>Consectetur Adipiscing Elit,<br>Sed Do Eiusmod Tempor Incididunt</p>
      <a>Learn More</a>
    </div>

    <div class="service" style="left:99px;top:311px">
      <div class="disc"><svg width="46" height="46" viewBox="0 0 46 46" fill="none" stroke="#fff" stroke-width="2.4"><rect x="7" y="9" width="32" height="28" rx="3"/><path d="M10 33l10-12 7 8 4-4 6 8"/><circle cx="31" cy="17" r="3"/></svg></div>
      <h3>Custom Images</h3>
      <p>"Lorem Ipsum Dolor Sit Amet,<br>Consectetur Adipiscing Elit,<br>Sed Do Eiusmod Tempor Incididunt</p>
      <a>Learn More</a>
    </div>

    <div class="service" style="left:598px;top:309px">
      <div class="disc"><svg width="46" height="46" viewBox="0 0 46 46" fill="none" stroke="#fff" stroke-width="2.2"><circle cx="21" cy="22" r="14"/><path d="M7 22h28M21 8c-6 7-6 21 0 28M21 8c6 7 6 21 0 28"/><path d="M32 26l7 3v5c0 4-3 6-7 7-4-1-7-3-7-7v-5z" fill="#2196e0"/></svg></div>
      <h3>Container Registry</h3>
      <p>"Lorem Ipsum Dolor Sit Amet,<br>Consectetur Adipiscing Elit,<br>Sed Do Eiusmod Tempor Incididunt</p>
      <a>Learn More</a>
    </div>

    <div class="service" style="left:91px;top:521px">
      <div class="disc"><svg width="46" height="46" viewBox="0 0 46 46" fill="none" stroke="#fff" stroke-width="2.4"><rect x="6" y="8" width="34" height="24" rx="2"/><path d="M17 38h12M23 32v6M11 16h12M11 21h16M11 26h8M34 12l-8 12"/></svg></div>
      <h3>Natively Integrated</h3>
      <p>"Lorem ipsum dolor sit amet,<br>consectetur adipiscing elit,<br>sed do eiusmod tempor incididunt</p>
      <a>Learn More</a>
    </div>

    <div class="service" style="left:605px;top:521px">
      <div class="disc"><svg width="46" height="46" viewBox="0 0 46 46" fill="none" stroke="#fff" stroke-width="2.2"><rect x="26" y="7" width="13" height="9"/><rect x="26" y="19" width="13" height="9"/><rect x="26" y="31" width="13" height="9"/><rect x="7" y="10" width="11" height="8"/><path d="M12 18v14M12 24h14M7 32h11v8H7z"/></svg></div>
      <h3>Stackform Provider</h3>
      <p>"Lorem Ipsum Dolor Sit Amet,<br>Consectetur Adipiscing Elit,<br>Sed Do Eiusmod Tempor Incididunt</p>
      <a>Learn More</a>
    </div>

    <div class="center-photo" role="img" aria-label="Smiling woman sitting cross-legged with a laptop in front of a server rack graphic"></div>
  </section>

  <!-- About -->
  <section class="section about">
    <h2>ABOUT HOSTING</h2>
    <div class="rule" style="left:72px;top:99px;width:181px"></div>
    <p>Lorem Ipsum Dolor Sit Amet, Consectetur Adipiscing Elit, Sed Do Eiusmod Tempor Incididunt Ut Labore Et Dolore Magna Aliqua. Ut Enim Ad Minim Veniam, Quis Nostrud Exercitation Ullamco Laboris Nisi Ut Aliquip Ex Ea Commodo Consequat. Lorem Ipsum Dolor Sit Amet, Consectetur Adipiscing Elit, Sed Do Eiusmod Tempor Incididunt Ut Labore Et Dolore Magna Aliqua. Ut Enim Ad Minim Veniam, Quis Nostrud Exercitation Ullamco Laboris Nisi Ut Aliquip Ex Ea Commodo Consequat.</p>
    <div class="btn-frame"></div>
    <div class="btn">Read More</div>
    <div class="photo-frame"></div>
    <div class="photo-back" role="img" aria-label="Businessman in a suit working at a desk with a coffee cup"></div>
    <div class="photo-front" role="img" aria-label="Woman in red working on a laptop in a sunlit cafe"></div>
  </section>

  <!-- Testimonials -->
  <section class="section testimonials">
    <h2 class="sec-title">TESTIMONIALS</h2>
    <div class="rule" style="left:364px;top:83px;width:176px;background:#fff"></div>
    <p class="sub">what our customer says</p>
    <svg class="arrow" style="left:32px;top:226px" viewBox="0 0 20 20"><path d="M13 3 6 10l7 7" fill="none" stroke="#fff" stroke-width="3.5"/></svg>
    <svg class="arrow" style="left:850px;top:226px" viewBox="0 0 20 20"><path d="M7 3l7 7-7 7" fill="none" stroke="#fff" stroke-width="3.5"/></svg>

    <div class="quote-card" style="left:113px">
      <svg width="38" height="28" viewBox="0 0 38 28"><path d="M2 28V14C2 6 7 1 15 0v6c-4 1-6 4-6 7h6v15zM22 28V14c0-8 5-13 13-14v6c-4 1-6 4-6 7h6v15z" fill="#0a58b4"/></svg>
      <p>Lorem Ipsum Dolor Sit Amet, Consectetur Adipiscing Elit,Sed Do Eiusmod Tempor Incididunt Ut Labore Et Dolore Magna Aliqua.Ut Enim Ad Minim Veniam, Quis Nostrud Exercitation Ullamco Laboris Nisi Ut Aliquip Ex Ea Commodo Consequat.Duis Aute Irure Dolor In Reprehenderit</p>
    </div>
    <div class="author" style="left:103px"><div class="ava" role="img" aria-label="Portrait of Owen Hale"></div><div><b>Owen Hale</b><span>Managing Director</span></div></div>

    <div class="quote-card" style="left:467px">
      <svg width="38" height="28" viewBox="0 0 38 28"><path d="M2 28V14C2 6 7 1 15 0v6c-4 1-6 4-6 7h6v15zM22 28V14c0-8 5-13 13-14v6c-4 1-6 4-6 7h6v15z" fill="#0a58b4"/></svg>
      <p>Lorem Ipsum Dolor Sit Amet, Consectetur Adipiscing Elit,Sed Do Eiusmod Tempor Incididunt Ut Labore Et Dolore Magna Aliqua.Ut Enim Ad Minim Veniam, Quis Nostrud Exercitation Ullamco Laboris Nisi Ut Aliquip Ex Ea Commodo Consequat.Duis Aute Irure Dolor In Reprehenderit</p>
    </div>
    <div class="author" style="left:459px"><div class="ava" role="img" aria-label="Portrait of Mira Stone"></div><div><b>Mira Stone</b><span>Assistant Manager</span></div></div>
  </section>

  <!-- Pricing -->
  <section class="section pricing">
    <h2 class="sec-title">OUR PRICING</h2>
    <div class="rule" style="left:346px;top:111px;width:212px"></div>
    <p class="lead">Lorem ipsum dolor sit amet, consectetur adipiscing elit, sed do eiusmod tempor incididunt<br>ut labore et dolore magna aliqua. Ut enim ad minim veniam,</p>
    <svg class="arrow" style="left:26px;top:341px" viewBox="0 0 20 20"><path d="M13 3 6 10l7 7" fill="none" stroke="#111" stroke-width="2"/></svg>
    <svg class="arrow" style="left:854px;top:341px" viewBox="0 0 20 20"><path d="M7 3l7 7-7 7" fill="none" stroke="#111" stroke-width="2"/></svg>

    <div class="plan" style="left:59px">
      <div class="ic"><svg width="44" height="42" viewBox="0 0 44 42" fill="none" stroke="#1a8ad4" stroke-width="2"><rect x="4" y="2" width="36" height="10"/><rect x="4" y="16" width="36" height="10"/><rect x="4" y="30" width="36" height="10"/><path d="M9 7h4M9 21h4M9 35h4M20 7h15M20 21h15M20 35h15"/></svg></div>
      <h4>Domain Registration</h4>
      <p>Lorem Ipsum Dolor Sit Amet, Conse Gbhy Hytfgh Okuij Ctetur Adipiscing Elit, Sed Do Eiusmod Tempor Incididunt Ut</p>
      <hr><div class="price"><em>£</em>24.99/month</div>
      <div class="go">GET STARTED NOW</div>
    </div>

    <div class="plan" style="left:260px">
      <div class="ic"><svg width="44" height="44" viewBox="0 0 44 44" fill="none" stroke="#1a8ad4" stroke-width="2.4"><circle cx="22" cy="22" r="19"/><path d="M3 22h38M22 3c-8 9-8 29 0 38M22 3c8 9 8 29 0 38"/><rect x="6" y="16" width="32" height="12" fill="#fff" stroke="none"/><text x="22" y="26" text-anchor="middle" font-family="Montserrat,sans-serif" font-size="10" font-weight="700" fill="#1a8ad4" stroke="none">www</text></svg></div>
      <h4>Web Hosting</h4>
      <p>Lorem Ipsum Dolor Sit Amet, Conse Gbhy Hytfgh Okuij Ctetur Adipiscing Elit, Sed Do Eiusmod Tempor Incididunt Ut</p>
      <hr><div class="price"><em>£</em>24.99/month</div>
      <div class="go">GET STARTED NOW</div>
    </div>

    <div class="plan featured" style="left:462px">
      <div class="ic"><svg width="46" height="46" viewBox="0 0 46 46" fill="none" stroke="#fff" stroke-width="2"><ellipse cx="16" cy="7" rx="11" ry="4"/><path d="M5 7v16c0 2 5 4 11 4s11-2 11-4V7M5 15c0 2 5 4 11 4s11-2 11-4"/><path d="M8 40a7 7 0 0 1 3-13 9 9 0 0 1 17 1 6 6 0 0 1 1 12z"/><circle cx="36" cy="24" r="5"/><path d="M36 16v3M36 29v3M28 24h3M41 24h3"/></svg></div>
      <h4>Free Web Builders</h4>
      <p>Lorem Ipsum Dolor Sit Amet, Conse Gbhy Hytfgh Okuij Ctetur Adipiscing Elit, Sed Do Eiusmod Tempor Incididunt Ut</p>
      <hr><div class="price"><em>£</em>24.99/month</div>
      <div class="go">GET STARTED NOW</div>
    </div>

    <div class="plan" style="left:662px">
      <div class="ic"><svg width="44" height="44" viewBox="0 0 44 44" fill="none" stroke="#1a8ad4" stroke-width="2"><rect x="3" y="3" width="10" height="14"/><rect x="31" y="3" width="10" height="8"/><rect x="3" y="29" width="10" height="12"/><rect x="31" y="29" width="10" height="12"/><path d="M13 10h18M8 17v12M36 11v18M8 23h28M18 33h8"/></svg></div>
      <h4>Dedicated Servers</h4>
      <p>Lorem Ipsum Dolor Sit Amet, Conse Gbhy Hytfgh Okuij Ctetur Adipiscing Elit, Sed Do Eiusmod Tempor Incididunt Ut</p>
      <hr><div class="price"><em>£</em>24.99/month</div>
      <div class="go">GET STARTED NOW</div>
    </div>
  </section>

  <!-- Footer -->
  <footer class="section footer">
    <div class="logo">BriarLoom</div>
    <p class="about-text">Lorem Ipsum Dolor Sit Amet,Consectetur Adipiscing Elit, Sed Do Eiusmod Tempor Incididunt Ut Labore Et Dolore Magn A Aliqua. Ut Enim Ad Minim Veniam,</p>
    <div class="follow">Follow Us</div>
    <div class="social" style="left:90px" aria-label="Social profile"><i></i></div>
    <div class="social" style="left:137px" aria-label="Social profile"><i></i></div>
    <div class="social" style="left:184px" aria-label="Social profile"><i></i></div>

    <div class="fcol" style="left:472px"><h5>Home</h5><ul><li>Home</li><li>Services</li><li>About Us</li><li>Join</li></ul></div>
    <div class="fcol" style="left:564px"><h5>Quick Links</h5><ul><li>Loremipsum</li><li>Loremipsum</li><li>Loremipsum</li><li>Loremipsum</li></ul></div>
    <div class="fcol" style="left:700px"><h5>Contact Us</h5><ul><li>#555-210-384</li><li>hello@briarloom.com</li></ul></div>

    <div class="divider"></div>
    <p class="copyright">Copyright 2021 BriarLoom<span></span>All Right Reserved</p>
  </footer>

</div>
</body>
</html>
```